Newspaper Ad for air cargo charter company

We need a 128x128mm color ad for an air cargo newspaper advertising our air charter services. Our main colors are blue.
You can see our website http://www.skyvaultfreight.com/cargo-charter/ for more information.
specifically the CARGO pages.
We want to promote that we are global, have fast response times, offer 24/7/365 service and that we are very competitive.

Target Market(s)

air cargo companies

Industry/Entity Type

It Company

Font styles to use
Sans Serif

Colors
0555a3
faa54b

Requirements
Must have
• a picture of loading a cargo airplane (i can provide)

```html
<!DOCTYPE html>
<html lang="en">
<head>
<meta charset="utf-8">
<title>SkyVault Freight – Cargo Charter</title>
<link href="https://fonts.googleapis.com/css2?family=Open+Sans:wght@400;600&family=Questrial&display=swap" rel="stylesheet">
<style>
  :root {
    --brand-blue: #0a47f0;
    --ink: #111111;
    --paper: #ffffff;
    --accent-orange: #faa54b;
    --sky-deep: #3a72c2;
    --sky-mid: #86aedd;
    --hull-white: #eef1f4;
    --hull-shade: #c4c9ce;
    --ground: #5a5e62;
  }
  html, body {
    margin: 0;
    padding: 0;
    overflow: hidden;
    background: var(--paper);
  }
  .ad {
    position: relative;
    width: 1200px;
    height: 1200px;
    overflow: hidden;
    background: var(--paper);
    font-family: "Questrial", sans-serif;
  }
  .ad__shapes {
    position: absolute;
    inset: 0;
  }
  .benefits {
    position: absolute;
    left: 32px;
    top: 244px;
    margin: 0;
    padding: 0;
    list-style: none;
    color: var(--ink);
    font-size: 48px;
    line-height: 38px;
    letter-spacing: -1.5px;
  }
  .benefits__item {
    position: relative;
    padding-left: 78px;
    margin-bottom: 24px;
  }
  .benefits__tick {
    position: absolute;
    left: 0;
    top: 50%;
    transform: translateY(-50%);
    width: 62px;
    height: 62px;
  }
  .brand {
    position: absolute;
    left: 38px;
    top: 690px;
    display: flex;
    align-items: center;
    gap: 16px;
  }
  .brand__dot {
    width: 34px;
    height: 34px;
    border-radius: 50%;
    background: var(--brand-blue);
  }
  .brand__name {
    font-family: "Open Sans", sans-serif;
    font-weight: 600;
    font-size: 46px;
    letter-spacing: 2px;
    color: var(--ink);
  }
  .cargo-icon {
    position: absolute;
    left: 940px;
    top: 695px;
    width: 175px;
    height: 170px;
  }
  .headline {
    position: absolute;
    right: 20px;
    top: 858px;
    margin: 0;
    font-family: "Open Sans", sans-serif;
    font-weight: 400;
    font-size: 82px;
    line-height: 1;
    letter-spacing: 1px;
    color: var(--paper);
  }
  .tagline {
    position: absolute;
    left: 480px;
    top: 962px;
    width: 720px;
    height: 54px;
    background: var(--accent-orange);
    color: var(--ink);
    font-family: "Open Sans", sans-serif;
    font-size: 34px;
    line-height: 54px;
    padding-left: 36px;
    box-sizing: border-box;
  }
  .contact {
    position: absolute;
    left: 30px;
    right: 20px;
    top: 1122px;
    display: flex;
    align-items: center;
    color: var(--paper);
  }
  .contact__item {
    display: flex;
    align-items: center;
    gap: 10px;
  }
  .contact__phone { font-size: 34px; letter-spacing: -1.5px; }
  .contact__web { font-size: 33px; margin-left: 36px; }
  .contact__address { font-size: 22px; line-height: 27px; margin-left: 34px; letter-spacing: 0.8px; }
  .contact__icon { fill: var(--paper); }
</style>
</head>
<body>
<div class="ad">
  <svg class="ad__shapes" width="1200" height="1200" viewBox="0 0 1200 1200">
    <defs>
      <linearGradient id="photoTone" x1="0.2" y1="0" x2="0.9" y2="1">
        <stop offset="0" stop-color="var(--sky-deep)"/>
        <stop offset="0.3" stop-color="var(--sky-mid)"/>
        <stop offset="0.5" stop-color="var(--hull-white)"/>
        <stop offset="0.66" stop-color="var(--hull-shade)"/>
        <stop offset="0.8" stop-color="var(--ground)"/>
      </linearGradient>
    </defs>
    <rect class="photo" x="0" y="0" width="1200" height="1200" fill="url(#photoTone)" role="img" aria-label="Photo: cargo being loaded through the raised nose door of a freighter aircraft on a scissor-lift loader under a blue sky"/>
    <polygon class="panel-white" points="0,0 212,0 690,752 0,1080" fill="var(--paper)"/>
    <polygon class="band-thin" points="0,1066 1200,478 1200,492 0,1080" fill="var(--brand-blue)"/>
    <polygon class="band-gap" points="0,1080 1200,492 1200,514 0,1104" fill="var(--paper)"/>
    <polygon class="band-main" points="0,1104 1200,514 1200,1200 0,1200" fill="var(--brand-blue)"/>
  </svg>

  <ul class="benefits">
    <li class="benefits__item"><svg class="benefits__tick" viewBox="0 0 60 60"><path d="M4 32 L14 26 L24 40 L50 4 L56 8 L26 56 Z" fill="var(--ink)"/></svg>global</li>
    <li class="benefits__item"><svg class="benefits__tick" viewBox="0 0 60 60"><path d="M4 32 L14 26 L24 40 L50 4 L56 8 L26 56 Z" fill="var(--ink)"/></svg>competitive</li>
    <li class="benefits__item"><svg class="benefits__tick" viewBox="0 0 60 60"><path d="M4 32 L14 26 L24 40 L50 4 L56 8 L26 56 Z" fill="var(--ink)"/></svg>fast response<br>times</li>
    <li class="benefits__item"><svg class="benefits__tick" viewBox="0 0 60 60"><path d="M4 32 L14 26 L24 40 L50 4 L56 8 L26 56 Z" fill="var(--ink)"/></svg>24/7, 365 days<br>service</li>
  </ul>

  <div class="brand">
    <span class="brand__dot"></span>
    <span class="brand__name">SKYVAULT FREIGHT</span>
  </div>

  <svg class="cargo-icon" viewBox="0 0 175 170" fill="none" stroke="var(--paper)" stroke-width="10" stroke-linejoin="round">
    <polygon points="10,40 95,8 165,45 80,80"/>
    <polygon points="10,40 80,80 80,162 14,122"/>
    <polygon points="80,80 165,45 163,125 80,162"/>
    <polygon points="40,28 120,52 120,70 40,45" fill="var(--paper)" stroke="none"/>
    <path d="M36 108 V80 M50 114 V86 M30 88 L36 78 L42 88 M44 94 L50 84 L56 94 M28 118 L58 132" stroke-width="5"/>
  </svg>

  <h1 class="headline">Cargo Charter</h1>
  <div class="tagline">Customized air transport is our specialty.</div>

  <div class="contact">
    <div class="contact__item contact__phone">
      <svg class="contact__icon" width="44" height="30" viewBox="0 0 44 30"><path d="M2 10 Q22 -4 42 10 L38 16 L30 12 L30 8 Q22 5 14 8 L14 12 L6 16 Z"/><path d="M10 14 H34 L40 28 H4 Z"/></svg>
      <span>+1-954-555-0148</span>
    </div>
    <div class="contact__item contact__web">
      <svg width="40" height="40" viewBox="0 0 40 40" fill="none" stroke="var(--paper)" stroke-width="2.5"><circle cx="20" cy="20" r="17"/><ellipse cx="20" cy="20" rx="8" ry="17"/><path d="M3 20 H37 M6 11 H34 M6 29 H34 M20 3 V37"/></svg>
      <span>www.skyvaultfreight.com</span>
    </div>
    <div class="contact__item contact__address">
      <svg class="contact__icon" width="30" height="44" viewBox="0 0 30 44"><path d="M15 1 C6 1 1 8 1 15 C1 26 15 43 15 43 C15 43 29 26 29 15 C29 8 24 1 15 1 Z M15 9 A6 6 0 1 1 15 21 A6 6 0 1 1 15 9 Z" fill-rule="evenodd"/></svg>
      <span>118 Harbor Way, Suite B<br>Fort Lauderdale, FL 33308</span>
    </div>
  </div>
</div>
</body>
</html>
```